Classic and neutral book cover design

We are looking for a classic and neutral book cover design to be used as the template for a series of books to be published. We are hence looking for a template that will allow us to easily change the title name for all books in this series.
The use of very few colours (black and white is welcome) and few design elements is a big bonus. As a source of inspiration we would like to ask you to view the very simple and
If you think you have a cool idea that can add a twist to the formal classic look don't hesitate. Go for it !
Work will be done for a 30 year old Sweden based cultural non-profit called VĂ©lra (www.velrafoundation.example). We work with the publishing and supporting of post-modern art and literature addressing contemporary topics but are also involved in assisting projects of cultural preservation.
Target Market(s)
The audience is expected to have some form of interest in culture but could range from hobbyist readers to tenure track scholars
Industry/Entity Type
Non-Profit
Requirements
Must have
- General:
- Classic and neutral feel
- Preferably very simple and few shapes
- usage of few colours (black and white is welcome)
Information to be displayed on the cover is:
- Author
- Title
- type of work e.g. play/novel (optional)
- publishing house (in this case "Velra Publishing")
Nice to have
- ideas to prevent it from become boring are of course welcome
Should not have
- - too many colours

```html
<!DOCTYPE html>
<html lang="en">
<head>
<meta charset="utf-8">
<title>Series Book Cover – Vélra Publishing</title>
<link rel="stylesheet" href="https://fonts.googleapis.com/css2?family=Tinos:wght@400&display=swap">
<style>
  :root {
    --page-bg: #ffffff;
    --cover-bg: #f7f7f6;
    --ink: #111111;
    --ornament-tone: rgba(40, 40, 40, 0.16);
    --ornament-fade: rgba(40, 40, 40, 0);
    --cover-shadow: rgba(0, 0, 0, 0.12);
  }

  html, body {
    margin: 0;
    padding: 0;
    width: 1000px;
    height: 1200px;
    overflow: hidden;
    background: var(--page-bg);
  }

  .canvas {
    position: relative;
    width: 1000px;
    height: 1200px;
    background: var(--page-bg);
  }

  .cover {
    position: absolute;
    left: 190px;
    top: 160px;
    width: 620px;
    height: 880px;
    background: var(--cover-bg);
    box-shadow: 0 12px 40px var(--cover-shadow);
    font-family: "Tinos", "Times New Roman", serif;
    color: var(--ink);
  }

  .cover-frame {
    position: absolute;
    left: 28px;
    top: 28px;
    width: 564px;
    height: 824px;
  }

  .ornament {
    position: absolute;
  }

  .ornament--top-left {
    left: 24px;
    top: 24px;
    width: 150px;
    height: 120px;
    border-top-left-radius: 4px;
    background: linear-gradient(135deg, var(--ornament-tone) 0%, var(--ornament-fade) 75%);
  }

  .ornament--bottom-right {
    right: 24px;
    bottom: 24px;
    width: 220px;
    height: 200px;
    border-bottom-right-radius: 4px;
    background: linear-gradient(315deg, var(--ornament-tone) 0%, var(--ornament-fade) 75%);
  }

  .cover-text {
    position: absolute;
    left: 0;
    width: 100%;
    margin: 0;
    text-align: center;
    font-weight: 400;
  }

  .cover-author {
    top: 170px;
    font-size: 30px;
  }

  .cover-title {
    top: 250px;
    font-size: 84px;
    letter-spacing: 1px;
    line-height: 1;
  }

  .cover-genre {
    top: 425px;
    font-size: 30px;
  }

  .cover-publisher {
    bottom: 50px;
    font-size: 26px;
    letter-spacing: 1px;
    text-transform: uppercase;
  }
</style>
</head>
<body>
  <main class="canvas">
    <section class="cover" aria-label="Book cover">
      <svg class="cover-frame" viewBox="0 0 564 824" width="564" height="824" aria-hidden="true">
        <polyline points="150,1 563,1 563,620" fill="none" stroke="#111111" stroke-width="2"/>
        <polyline points="1,130 1,823 360,823" fill="none" stroke="#111111" stroke-width="2"/>
      </svg>

      <div class="ornament ornament--top-left" role="img" aria-label="Black floral flourish ornament in the top-left corner"></div>
      <div class="ornament ornament--bottom-right" role="img" aria-label="Black floral flourish ornament in the bottom-right corner"></div>

      <p class="cover-text cover-author">Author</p>
      <h1 class="cover-text cover-title">TITLE</h1>
      <p class="cover-text cover-genre">novel</p>
      <p class="cover-text cover-publisher">Vélra</p>
    </section>
  </main>
</body>
</html>
```